Business Card and Letterhead for new company Corvalt GreenWorks, Inc.

Corvalt GreenWorks, Inc., an engineering and construction firm that provides services for solid waste landfill gas systems, needs a business card and letterhead. We recently had a logo designed but we are open to some tweaks to logo design and color scheme. Generally, we like "earthy" color tones - greens, browns, oranges. This is a sister company - www.taldrickengineering.example.

Target Market(s)

Solid waste landfill companies - Binford Disposal, Keystell Holdings, etc.

Industry/Entity Type

Engineering and Construction

Contact Information for Business Card

Name, Title, email, mobile phone, work phone, website. Potential list of services for back of card: LFG Engineering and Design, GCCS Planning and Operational Consulting, Compliance Monitoring and Reporting, Routine Operations & Maintenance, Nonroutine O&M, Construction Management, Construction QA, GCCS Construction

Font styles to use
Sans Serif

Requirements
Must have
• Logo, pertinent information, maybe a tagline (still in development)
Nice to have
• For back of card, considering an engineering scale (attached for another business of ours), but want to look at other options, alternatives. Like the idea of the back of card to have some utility (scale, unit conversion info, list of services) but willing to consider lots of options.
Should not have
• Needs to have a professional (engineering) and technical look, not cartoonish.

```html
<!DOCTYPE html>
<html lang="en">
<head>
<meta charset="utf-8">
<title>Corvalt GreenWorks – Stationery</title>
<link href="https://fonts.googleapis.com/css2?family=Mulish:wght@400;600;700;800&display=swap" rel="stylesheet">
<style>
  :root {
    --backdrop: #b3b3b3;
    --paper: #ffffff;
    --brand-green: #6db33f;
    --brand-grey: #7b7d80;
    --text-grey: #6f7175;
    --faint-grey: #e4e5e6;
    --faint-green: #e6f0dc;
  }
  * { margin: 0; padding: 0; box-sizing: border-box; }
  html, body { width: 1200px; height: 1000px; overflow: hidden; }
  body {
    background: var(--backdrop);
    font-family: "Mulish", Arial, sans-serif;
    position: relative;
  }
  .sheet { position: absolute; background: var(--paper); overflow: hidden; }

  /* Letterhead */
  .letterhead { left: 110px; top: 137px; width: 507px; height: 696px; }
  .brand-mark {
    position: absolute; display: flex; align-items: center; gap: 6px;
    font-weight: 800; color: var(--brand-grey); line-height: 1.05;
  }
  .brand-mark .dot { width: 10px; height: 10px; border-radius: 50%; background: var(--brand-green); flex: none; }
  .letterhead .brand-mark { left: 33px; top: 70px; font-size: 17px; }
  .watermark {
    position: absolute; font-weight: 800; line-height: 0.95;
    color: var(--faint-grey); white-space: nowrap;
  }
  .letterhead .watermark { left: 38px; top: 300px; font-size: 64px; }
  .letterhead-footer {
    position: absolute; right: 26px; top: 634px;
    font-size: 10.5px; color: var(--text-grey); text-align: right; line-height: 13px;
  }
  .contact-line { display: flex; align-items: center; justify-content: flex-end; gap: 6px; }
  .icon { width: 8px; height: 8px; flex: none; }

  /* Card front */
  .card-front { left: 678px; top: 344px; width: 399px; height: 229px; }
  .card-front .watermark { left: 205px; top: 70px; font-size: 46px; color: var(--faint-green); }
  .card-front .brand-mark { left: 127px; top: 34px; font-size: 15px; }
  .holder { position: absolute; right: 215px; top: 116px; text-align: right; }
  .holder-name { font-size: 13px; font-weight: 700; color: var(--brand-green); }
  .holder-title { font-size: 13px; color: var(--text-grey); margin-top: 2px; }
  .divider { position: absolute; left: 194px; top: 116px; width: 1px; height: 37px; background: var(--brand-green); }
  .card-contacts { position: absolute; left: 206px; top: 115px; font-size: 10px; color: var(--text-grey); line-height: 13px; }
  .card-contacts .contact-line { justify-content: flex-start; }
  .card-site { position: absolute; right: 139px; top: 203px; font-size: 10.5px; color: var(--text-grey); }
  .card-site strong { color: var(--brand-green); font-weight: 700; }

  /* Card back */
  .card-back { left: 678px; top: 605px; width: 399px; height: 228px; }
  .services { position: absolute; left: 20px; top: 47px; list-style: none; font-size: 12px; color: var(--text-grey); line-height: 19.6px; letter-spacing: 0.2px; }
  .services li::before { content: "•"; color: var(--brand-green); margin-right: 5px; }
  .card-back .brand-mark { right: 20px; top: 168px; font-size: 14px; }
</style>
</head>
<body>

<section class="sheet letterhead">
  <div class="brand-mark"><span class="dot"></span><span>Corvalt<br>GreenWorks</span></div>
  <div class="watermark" aria-hidden="true">Corvalt<br>GreenWorks</div>
  <div class="letterhead-footer">
    <div class="contact-line">office phone
      <svg class="icon" viewBox="0 0 10 10"><path d="M2 1l2 2-1 1.2c.6 1.2 1.6 2.2 2.8 2.8L7 6l2 2-1.2 1.2C4.5 9 1 5.5.8 2.2z" fill="var(--brand-green)"/></svg></div>
    <div class="contact-line">email@corvaltgreenworks.example
      <svg class="icon" viewBox="0 0 10 10"><rect x="0.5" y="2" width="9" height="6.5" fill="var(--brand-green)"/><path d="M0.5 2l4.5 3.5L9.5 2" stroke="#fff" fill="none"/></svg></div>
    <div class="contact-line">corvaltgreenworks.example
      <svg class="icon" viewBox="0 0 10 10"><circle cx="5" cy="5" r="4.2" fill="var(--brand-green)"/><path d="M1 5h8M5 1v8" stroke="#fff" stroke-width=".8"/></svg></div>
  </div>
</section>

<section class="sheet card-front">
  <div class="watermark" aria-hidden="true">Corvalt<br>Green<br>Works</div>
  <div class="brand-mark"><span class="dot"></span><span>Corvalt<br>GreenWorks</span></div>
  <div class="holder">
    <div class="holder-name">Employee Name</div>
    <div class="holder-title">Title</div>
  </div>
  <div class="divider"></div>
  <div class="card-contacts">
    <div class="contact-line"><svg class="icon" viewBox="0 0 10 10"><rect x="2.5" y="0.5" width="5" height="9" rx="1" fill="none" stroke="var(--brand-green)" stroke-width="1.2"/></svg>mobile phone</div>
    <div class="contact-line"><svg class="icon" viewBox="0 0 10 10"><path d="M2 1l2 2-1 1.2c.6 1.2 1.6 2.2 2.8 2.8L7 6l2 2-1.2 1.2C4.5 9 1 5.5.8 2.2z" fill="var(--brand-green)"/></svg>office phone</div>
    <div class="contact-line"><svg class="icon" viewBox="0 0 10 10"><rect x="0.5" y="2" width="9" height="6.5" fill="var(--brand-green)"/><path d="M0.5 2l4.5 3.5L9.5 2" stroke="#fff" fill="none"/></svg>email@corvaltgreenworks.example</div>
  </div>
  <div class="card-site"><strong>corvaltgreenworks</strong>.example</div>
</section>

<section class="sheet card-back">
  <ul class="services">
    <li>LFG Engineering and Design</li>
    <li>GCCS Planning and Operational Consulting</li>
    <li>Compliance Monitoring and Reporting</li>
    <li>Routine Operations &amp; Maintenance</li>
    <li>Nonroutine O&amp;M</li>
    <li>Construction Management</li>
    <li>Construction QA</li>
    <li>GCCS Construction</li>
  </ul>
  <div class="brand-mark"><span class="dot"></span><span>Corvalt<br>GreenWorks</span></div>
</section>

</body>
</html>
```